Dovecrest Trailers LLC

We need a flier designed to market our trailers. We would like to showcase some of the trailers we sell. Also we would like to target landscaping companies, construction companies, also for home use and recreational use.

```html
<!DOCTYPE html>
<html lang="en">
<head>
<meta charset="utf-8">
<title>Dovecrest Trailers LLC – Landscaping Construction Flier</title>
<link href="https://fonts.googleapis.com/css2?family=Bebas+Neue&family=Quicksand:wght@400;500&display=swap" rel="stylesheet">
<style>
  :root {
    --page-bg: #ffffff;
    --orange: #ef6a22;
    --orange-clear: rgba(239, 106, 34, 0);
    --ink: #111111;
    --white: #ffffff;
    --photo-top: #7fa6cc;
    --photo-bottom: #6a9e3a;
    --badge-ring: #8a8a8a;
  }
  * { box-sizing: border-box; margin: 0; padding: 0; }
  html, body {
    width: 1200px;
    height: 1200px;
    overflow: hidden;
    background: var(--page-bg);
  }
  .flier {
    position: absolute;
    left: 229px;
    top: 75px;
    width: 742px;
    height: 1050px;
    overflow: hidden;
    font-family: "Quicksand", sans-serif;
  }
  .flier__photo {
    position: absolute;
    inset: 0;
    background: linear-gradient(to bottom, var(--photo-top) 0%, var(--photo-bottom) 100%);
  }
  .flier__facet {
    position: absolute;
    left: 0;
    top: 0;
    width: 742px;
    height: 260px;
  }
  .flier__panel {
    position: absolute;
    left: 0;
    top: 0;
    width: 481px;
    height: 100%;
    background: linear-gradient(to bottom,
      var(--orange-clear) 0%,
      rgba(239, 106, 34, 0.25) 22%,
      rgba(239, 106, 34, 0.7) 36%,
      var(--orange) 52%,
      var(--orange) 100%);
  }
  .brand-badge {
    position: absolute;
    left: 486px;
    top: 15px;
    width: 220px;
    height: 220px;
    border-radius: 50%;
    background: var(--white);
    border: 4px solid var(--badge-ring);
    display: flex;
    align-items: center;
    justify-content: center;
    text-align: center;
  }
  .brand-badge__name {
    font-family: "Quicksand", sans-serif;
    font-weight: 500;
    font-size: 24px;
    line-height: 1.2;
    color: var(--orange);
  }
  .headline {
    position: absolute;
    left: 43px;
    top: 334px;
    font-family: "Bebas Neue", sans-serif;
    font-weight: 400;
    font-size: 92px;
    line-height: 1.2;
    color: var(--ink);
    letter-spacing: 0.3px;
  }
  .intro {
    position: absolute;
    left: 44px;
    top: 582px;
    width: 420px;
    font-size: 17.5px;
    line-height: 22.2px;
    color: var(--white);
  }
  .divider {
    position: absolute;
    left: 204px;
    top: 924px;
    width: 277px;
    height: 16px;
  }
  .divider__mark {
    position: absolute;
    left: 0;
    top: 0;
    width: 16px;
    height: 16px;
    background: var(--white);
  }
  .divider__line {
    position: absolute;
    left: 16px;
    right: 0;
    top: 7px;
    height: 2px;
    background: var(--white);
  }
  .contact {
    position: absolute;
    left: 44px;
    top: 967px;
    list-style: none;
    color: var(--white);
    font-size: 17.5px;
    line-height: 23px;
  }
  .contact__item {
    display: flex;
    align-items: center;
    gap: 9px;
  }
  .contact__icon {
    width: 15px;
    height: 15px;
    flex: none;
  }
</style>
</head>
<body>
  <main class="flier">
    <div class="flier__photo" role="img" aria-label="Photo area: a brick house with trimmed shrubs and a green lawn under a blue sky"></div>

    <svg class="flier__facet" viewBox="0 0 742 260" aria-hidden="true">
      <polygon points="0,0 459,0 359,181" fill="#ffffff" fill-opacity="0.16"/>
    </svg>

    <div class="flier__panel"></div>

    <div class="brand-badge">
      <span class="brand-badge__name">Dovecrest<br>Trailers LLC</span>
    </div>

    <h1 class="headline">Landscaping<br>Construction</h1>

    <p class="intro">Dovecrest Trailers LLC builds tough, dependable trailers for the crews who shape every yard and job site. Haul mowers, mulch, pavers and tools with our open utility trailers, or move heavy machines and materials on our equipment and dump models. We also carry enclosed and light trailers for home projects, moving day and weekend trips with bikes, boats and ATVs. Every trailer is built with steel frames, sealed wiring and strong axles. Visit our lot, compare models side by side and let our team help you find the right fit.</p>

    <div class="divider" aria-hidden="true">
      <span class="divider__mark"></span>
      <span class="divider__line"></span>
    </div>

    <ul class="contact">
      <li class="contact__item">
        <svg class="contact__icon" viewBox="0 0 24 24" aria-hidden="true">
          <path fill="#ffffff" d="M6.6 10.8a15.2 15.2 0 0 0 6.6 6.6l2.2-2.2a1 1 0 0 1 1-.25 11.4 11.4 0 0 0 3.6.57 1 1 0 0 1 1 1V20a1 1 0 0 1-1 1A17 17 0 0 1 3 4a1 1 0 0 1 1-1h3.5a1 1 0 0 1 1 1c0 1.25.2 2.45.57 3.57a1 1 0 0 1-.25 1z"/>
        </svg>
        <span>1234567890</span>
      </li>
      <li class="contact__item">
        <svg class="contact__icon" viewBox="0 0 24 24" aria-hidden="true">
          <rect x="2" y="5" width="20" height="14" rx="1.5" fill="#ffffff"/>
        </svg>
        <span>contact@website.com</span>
      </li>
    </ul>
  </main>
</body>
</html>
```